I am looking for a modern, clean and neat design for a reflexology and well being business. The business name is Lumen Orto (this is an old Latin word for wellbeing). The colours I would like are purple, white and grey. I am open to suggestions for pictures such as healing or working hands, a pair of feet, images that represent my business that you may think of....... or maybe you think no images at all would be best? My tag line is: "Relax, Renew, Revive" or "Find you balance......... Relax, Renew, Revive" I can decide which I want so I would like to see what both would look like. I would like space on the back to write the client's appointment date and time (more than once)

```html
<!DOCTYPE html>
<html lang="en">
<head>
<meta charset="utf-8">
<title>Lumen Orto – Business Card</title>
<link href="https://fonts.googleapis.com/css2?family=Open+Sans:wght@400;600;700&display=swap" rel="stylesheet">
<style>
  :root {
    --bg: #2b2b2d;
    --card-dark: #4b4b4d;
    --card-light: #ffffff;
    --lavender: #9fb3dd;
    --ink: #3e3e40;
    --white: #ffffff;
  }
  * { margin: 0; padding: 0; box-sizing: border-box; }
  html, body { width: 1200px; height: 900px; overflow: hidden; background: var(--bg); font-family: "Open Sans", sans-serif; }
  .stage { position: relative; width: 1200px; height: 900px; }
  .card { position: absolute; width: 580px; height: 332px; border-radius: 22px; overflow: hidden; }

  /* Back */
  .card-back { left: 70px; top: 80px; background: var(--card-dark); color: var(--white); }
  .brand { position: absolute; display: flex; align-items: center; gap: 10px; font-weight: 400; letter-spacing: 1px; white-space: nowrap; }
  .brand-dot { width: 22px; height: 22px; border-radius: 50%; background: var(--lavender); }
  .card-back .brand { left: 170px; top: 96px; font-size: 22px; color: var(--white); }
  .tagline { position: absolute; right: 40px; top: 48px; font-size: 12px; font-weight: 600; letter-spacing: .5px; white-space: nowrap; }
  .appointment { position: absolute; left: 40px; top: 168px; right: 40px; }
  .appointment h2 { font-size: 19px; font-weight: 700; margin-bottom: 6px; }
  .field { display: flex; align-items: flex-end; font-size: 13px; height: 30px; }
  .field span { margin-right: 6px; }
  .field i { flex: 1; border-bottom: 2px dotted rgba(255,255,255,.8); margin-bottom: 4px; }

  /* Front */
  .card-front { left: 550px; top: 478px; background: var(--card-light); }
  .card-front .brand { right: 44px; top: 48px; font-size: 22px; color: var(--ink); }
  .bands { position: absolute; inset: 0; width: 100%; height: 100%; }
  .person { position: absolute; left: 36px; top: 150px; }
  .person-name { font-size: 23px; font-weight: 700; color: var(--lavender); letter-spacing: 1px; line-height: 1.1; }
  .person-role { font-size: 12px; font-weight: 600; color: var(--ink); letter-spacing: .5px; margin-bottom: 6px; }
  .contact { list-style: none; font-size: 13px; color: var(--ink); }
  .contact li { display: flex; align-items: center; gap: 8px; line-height: 1.45; }
  .contact svg { width: 11px; height: 11px; fill: var(--lavender); flex: none; }
</style>
</head>
<body>
<main class="stage">
  <section class="card card-back">
    <p class="tagline">RELAX, RENEW, REVIVE</p>
    <div class="brand"><span class="brand-dot"></span>LUMEN ORTO</div>
    <div class="appointment">
      <h2>Appointment:</h2>
      <div class="field"><span>Name:</span><i></i></div>
      <div class="field"><span>Time:</span><i></i></div>
      <div class="field"><span>Date:</span><i></i></div>
    </div>
  </section>

  <section class="card card-front">
    <svg class="bands" viewBox="0 0 580 332" preserveAspectRatio="none" aria-hidden="true">
      <polygon points="0,332 0,320 440,236 580,236 580,332" fill="#4b4b4d"/>
      <polygon points="440,236 452,176 580,146 580,236" fill="#9fb3dd"/>
    </svg>
    <div class="brand"><span class="brand-dot"></span>LUMEN ORTO</div>
    <div class="person">
      <p class="person-name">CLARA VOSS</p>
      <p class="person-role">DIRECTOR</p>
      <ul class="contact">
        <li><svg viewBox="0 0 12 12"><path d="M2 1l2 0 1 3-1.5 1a6 6 0 0 0 3 3L7.5 6.5l3 1 0 2A1.5 1.5 0 0 1 9 11 9 9 0 0 1 1 3 1.5 1.5 0 0 1 2 1z"/></svg>+330 5550-1284</li>
        <li><svg viewBox="0 0 12 12"><path d="M1 2h10v8H1z M1 2l5 4 5-4" fill="none" stroke="#9fb3dd" stroke-width="1.4"/></svg>info@lumenortomail.com</li>
        <li><svg viewBox="0 0 12 12"><circle cx="6" cy="6" r="5"/></svg>www.lumenorto.com</li>
      </ul>
    </div>
  </section>
</main>
</body>
</html>
```